Plakat für Verein
Zielgruppe
Wir möchten eine Veranstaltung für unseren Verein - Hinterkalmbacher Heimatpflegeverein machen.
Aufgabenstellung
Die Party der Golden 20er
Glanz-Glamour-Lebenslust
Tanzen wie früher - Feiern wie nie
21. März - Uhrzeit: 20.30 im Saal KM
Live mit DJaneMarlies
Dresscode: Goldene 20er - Fransen, Federn, Hosenträger, Zylinder
Farbe: Gold/Schgwarz

```html
<!DOCTYPE html>
<html lang="de">
<head>
<meta charset="utf-8">
<title>Die Party der Golden 20er – Plakat</title>
<link rel="stylesheet" href="https://fonts.googleapis.com/css2?family=Limelight&family=Josefin+Slab:wght@400;600;700&display=swap">
<style>
  :root {
    --page: #ececec;
    --ink: #16131a;
    --gold: #c09a4e;
    --gold-deep: #8f6f2a;
    --white: #ffffff;
  }
  * { margin: 0; padding: 0; box-sizing: border-box; }
  html, body {
    width: 1200px; height: 848px; overflow: hidden;
    background: var(--page);
  }
  .poster {
    position: absolute; left: 310px; top: 14px;
    width: 580px; height: 820px;
    background: var(--ink);
    overflow: hidden;
    font-family: "Josefin Slab", Georgia, serif;
    color: var(--white);
  }
  .deco-band {
    position: absolute; left: 0; top: 0; width: 100%; height: 96px;
    background: linear-gradient(180deg, var(--gold-deep) 0%, #4a3a1c 45%, var(--ink) 100%);
  }
  .title {
    position: absolute; left: 0; width: 100%; text-align: center;
    font-family: "Limelight", Georgia, serif;
    color: var(--gold); line-height: 1; letter-spacing: 2px;
    white-space: nowrap;
  }
  .title--one { top: 102px; font-size: 50px; }
  .title--two { top: 172px; font-size: 52px; }
  .title small { font-size: 26px; letter-spacing: 1px; }
  .rule {
    position: absolute; left: 29px; width: 522px; height: 10px;
  }
  .rule--top { top: 242px; }
  .rule--bottom { top: 725px; }
  .slogan {
    position: absolute; left: 0; width: 100%; text-align: center;
    white-space: nowrap; line-height: 1;
  }
  .slogan--main { top: 258px; font-size: 31px; letter-spacing: 1px; }
  .slogan--sub { top: 302px; font-size: 24px; letter-spacing: 0.5px; }
  .sep {
    display: inline-block; width: 7px; height: 7px;
    border: 1.5px solid var(--white); vertical-align: middle;
    margin: 0 8px 6px;
  }
  .date-badge {
    position: absolute; left: 25px; top: 355px; width: 256px; height: 256px;
  }
  .date-text {
    position: absolute; left: 25px; top: 412px; width: 256px;
    text-align: center; font-size: 31px; line-height: 39px; letter-spacing: 1px;
  }
  .illustration {
    position: absolute; left: 270px; top: 405px; width: 310px; height: 313px;
    background: radial-gradient(circle at 55% 40%, var(--gold) 0%, var(--gold-deep) 55%, #2a2230 100%);
    border-radius: 160px 0 0 0;
  }
  .live {
    position: absolute; left: 25px; top: 638px; width: 256px;
    text-align: center; color: var(--gold); font-weight: 700;
    font-size: 24px; line-height: 29px;
  }
  .dresscode {
    position: absolute; left: 0; width: 100%; text-align: center;
    white-space: nowrap; line-height: 1;
  }
  .dresscode--label { top: 736px; font-size: 20px; letter-spacing: 1px; }
  .dresscode--label small { font-size: 12px; }
  .dresscode--items { top: 766px; font-size: 21px; letter-spacing: 0.5px; }
  .dresscode--items .sep { width: 6px; height: 6px; margin: 0 7px 5px; }
</style>
</head>
<body>
  <main class="poster">
    <div class="deco-band" role="img" aria-label="Art-Déco-Fächerornamente in Gold"></div>

    <h1 class="title title--one">DIE PARTY</h1>
    <p class="title title--two">DER GOLDEN 20<small>ER</small></p>

    <svg class="rule rule--top" viewBox="0 0 522 10" aria-hidden="true">
      <rect x="1" y="1" width="8" height="8" fill="none" stroke="#c09a4e" stroke-width="1.5"/>
      <rect x="513" y="1" width="8" height="8" fill="none" stroke="#c09a4e" stroke-width="1.5"/>
      <line x1="9" y1="3.5" x2="513" y2="3.5" stroke="#c09a4e" stroke-width="1"/>
      <line x1="9" y1="6.5" x2="513" y2="6.5" stroke="#c09a4e" stroke-width="1"/>
    </svg>

    <p class="slogan slogan--main">GLANZ<span class="sep"></span>GLAMOUR<span class="sep"></span>LEBENSLUST</p>
    <p class="slogan slogan--sub">TANZEN WIE FRÜHER<span class="sep"></span>FEIERN WIE NIE</p>

    <svg class="date-badge" viewBox="0 0 256 256" aria-hidden="true">
      <circle cx="128" cy="128" r="124" fill="none" stroke="#c09a4e" stroke-width="1.5"/>
      <circle cx="128" cy="128" r="110" fill="none" stroke="#c09a4e" stroke-width="1.5"/>
      <circle cx="128" cy="128" r="102" fill="#8f6f2a"/>
    </svg>
    <p class="date-text">21. MÄRZ<br>20.30 UHR<br>SAAL KM</p>

    <div class="illustration" role="img" aria-label="Illustriertes Tanzpaar im Stil der 1920er Jahre vor goldenem Kreis"></div>

    <p class="live">Live mit<br>DJaneMarlies</p>

    <svg class="rule rule--bottom" viewBox="0 0 522 10" aria-hidden="true">
      <rect x="1" y="1" width="8" height="8" fill="none" stroke="#c09a4e" stroke-width="1.5"/>
      <rect x="513" y="1" width="8" height="8" fill="none" stroke="#c09a4e" stroke-width="1.5"/>
      <line x1="9" y1="3.5" x2="513" y2="3.5" stroke="#c09a4e" stroke-width="1"/>
      <line x1="9" y1="6.5" x2="513" y2="6.5" stroke="#c09a4e" stroke-width="1"/>
    </svg>

    <p class="dresscode dresscode--label">GOLDENE 20<small>ER</small> DRESSCODE:</p>
    <p class="dresscode dresscode--items">FRANSEN<span class="sep"></span>FEDERN<span class="sep"></span>HOSENTRÄGER<span class="sep"></span>ZYLINDER</p>
  </main>
</body>
</html>
```